*** Business Card Design Project

I need a logo and business card for my new catering business: "Pomelia". The design should be modern, clean, elegant and refined. One or Two colours only. The design SHOULD NOT include graphics or images. There should be space for my name, phone number and email address (I will provide these to you later).

Industry/Entity Type

Catering

Requirements
Must have
• Must have one or two colours only.
Must include the text "pomelia"
Should not have
• Must not have graphics or images.

```html
<!DOCTYPE html>
<html lang="en">
<head>
<meta charset="utf-8">
<title>Pomelia – Business Card</title>
<link rel="stylesheet" href="https://fonts.googleapis.com/css2?family=Antonio:wght@300&family=Barlow:wght@400&display=swap">
<style>
  :root {
    --card-bg: #1f2326;
    --accent: #d4f70f;
  }
  html, body {
    margin: 0;
    padding: 0;
    width: 1200px;
    height: 741px;
    overflow: hidden;
    background: var(--card-bg);
  }
  .card {
    position: relative;
    width: 1200px;
    height: 741px;
    background: var(--card-bg);
    color: var(--accent);
  }
  .brand-name {
    position: absolute;
    right: 792px;
    top: 448px;
    margin: 0;
    font-family: "Antonio", sans-serif;
    font-weight: 300;
    font-size: 42px;
    line-height: 1;
    letter-spacing: 0.5px;
  }
  .divider {
    position: absolute;
    left: 0;
    top: 0;
  }
  .person-name,
  .website {
    position: absolute;
    top: 405px;
    margin: 0;
    font-family: "Antonio", sans-serif;
    font-weight: 300;
    font-size: 52px;
    line-height: 1;
    text-transform: uppercase;
    letter-spacing: -0.5px;
  }
  .person-name { left: 441px; }
  .website { right: 67px; }
  .contact {
    position: absolute;
    right: 57px;
    top: 493px;
    margin: 0;
    font-family: "Barlow", sans-serif;
    font-weight: 400;
    font-size: 30px;
    line-height: 46px;
    letter-spacing: 1px;
    text-align: right;
    font-style: normal;
  }
  .contact span { display: block; }
</style>
</head>
<body>
  <main class="card">
    <p class="brand-name">POMELIA</p>
    <svg class="divider" width="1200" height="741" viewBox="0 0 1200 741" aria-hidden="true">
      <line x1="418" y1="475" x2="1200" y2="475" stroke="var(--accent)" stroke-width="4.5"/>
    </svg>
    <h1 class="person-name">Marta Quinlan</h1>
    <p class="website">www.pomelia.com</p>
    <address class="contact">
      <span class="email">marta@pomelia.com</span>
      <span class="phone">Phone:899.410.372</span>
    </address>
  </main>
</body>
</html>
```